Brightpath Dentistry - Flyer - Modern & Eye catching campaign flyer

Need front & back side full page flyer designs for both 1) Grand opening 2) On-going campaign.

Attached the new dental office logo.
Attached our other dental clinic flyer designs for content.

Target Market(s)

Cosmetic dentistry

Industry/Entity Type

Health Care

Requirements
Must have
• decent, modern and eye catching marketing flyers.
Nice to have
• - Nice space
• - Highlight phone number
• - Highlight special features like convenient hours, call or text, for all ages, digital facility, etc
Should not have
• - Don't want to fill the flyer with too much wordings
• - Too many colors

```html
<!DOCTYPE html>
<html lang="en">
<head>
<meta charset="utf-8">
<title>Brightpath Dentistry – Grand Opening Flyer</title>
<link rel="stylesheet" href="https://fonts.googleapis.com/css2?family=Lato:wght@400;700;900&family=Yellowtail&display=swap">
<style>
  :root {
    --teal: #2fa3bd;
    --teal-deep: #1f8aa6;
    --navy: #1d5f9e;
    --white: #ffffff;
    --mist: #e9eef1;
    --stage: #1c1c1c;
  }
  * { box-sizing: border-box; margin: 0; padding: 0; }
  html, body { width: 1200px; height: 800px; overflow: hidden; }
  body { background: var(--stage); font-family: "Lato", Arial, sans-serif; position: relative; }

  .flyer {
    position: absolute; left: 330px; top: 18px; width: 540px; height: 764px;
    background: linear-gradient(180deg, #f4f6f7 0%, var(--mist) 45%, #ffffff 100%);
    overflow: hidden;
  }
  .flyer-shapes { position: absolute; inset: 0; }

  .hero-photo {
    position: absolute; left: 160px; top: 24px; width: 240px; height: 290px;
    border-radius: 120px 120px 12px 12px;
    background: linear-gradient(180deg, #cfdde4 0%, #c9a48d 45%, #b7c9d2 100%);
  }
  .headrest {
    position: absolute; left: 124px; top: 180px; width: 64px; height: 110px;
    border-radius: 32px; background: linear-gradient(160deg, #4fb2e6, #1769a8);
  }

  .brand { position: absolute; right: 28px; top: 48px; display: flex; align-items: center; gap: 8px; }
  .brand-dot { width: 22px; height: 22px; border-radius: 50%; background: var(--navy); }
  .brand-name { color: var(--navy); font-weight: 700; font-size: 19px; white-space: nowrap; }

  .call-pill {
    position: absolute; right: 20px; top: 92px; width: 228px; height: 70px;
    border-radius: 35px; background: var(--teal); border: 5px solid var(--navy);
    color: var(--white); text-align: center; box-shadow: 0 0 0 3px var(--white) inset;
    padding-top: 6px;
  }
  .call-label { font-size: 15px; }
  .call-number { font-size: 30px; font-weight: 900; letter-spacing: .5px; line-height: 1.05; white-space: nowrap; }

  .circle {
    position: absolute; border-radius: 50%; border: 6px solid var(--white);
    box-shadow: 0 3px 8px rgba(0,0,0,.2);
  }
  .photo-family { left: 26px; top: 240px; width: 150px; height: 150px;
    background: linear-gradient(150deg, #c9a48d, #7b8a96 60%, #3b3f48); }
  .photo-kids { left: 172px; top: 238px; width: 104px; height: 104px;
    background: linear-gradient(150deg, #e9cdb8, #c8a890 55%, #7aa36a); }
  .offer {
    background: var(--teal); color: var(--white); display: flex; align-items: center;
    justify-content: center; text-align: center; font-weight: 700; line-height: 1.15;
    font-size: 15px;
  }
  .offer-treatment { left: 284px; top: 232px; width: 104px; height: 104px; }
  .offer-kids { left: 262px; top: 336px; width: 112px; height: 112px; }
  .offer-adults { left: 150px; top: 360px; width: 114px; height: 114px; }

  .tooth-art {
    position: absolute; right: 22px; top: 336px; width: 118px; height: 180px;
    border-radius: 45% 45% 30% 30%;
    background: linear-gradient(180deg, #d9b23c 0%, #d9b23c 22%, #f4f6f7 24%, #cfd6da 100%);
  }

  .headline {
    position: absolute; left: 36px; top: 478px; width: 400px;
    font-family: "Yellowtail", "Brush Script MT", cursive; font-weight: 400;
    font-size: 70px; line-height: 80px; white-space: nowrap;
    color: var(--white); text-shadow: 0 3px 6px rgba(0,0,0,.25);
  }
  .hours-pill {
    position: absolute; left: 44px; top: 566px; width: 410px; height: 36px;
    border-radius: 18px; background: var(--white); border: 3px solid var(--navy);
    color: var(--teal-deep); font-size: 17px; font-weight: 700; text-align: center;
    line-height: 30px; letter-spacing: .5px; white-space: nowrap;
  }
  .hours-pill strong { color: var(--navy); font-weight: 900; }
  .fine-print { position: absolute; left: 60px; top: 610px; color: var(--white); font-size: 12px; white-space: nowrap; }
  .welcome {
    position: absolute; left: 40px; top: 630px; color: var(--white);
    font-size: 30px; line-height: 38px; font-weight: 900; letter-spacing: .3px; white-space: nowrap;
  }

  .contact { position: absolute; color: var(--teal-deep); font-size: 15px; font-weight: 700;
    display: flex; align-items: center; gap: 7px; white-space: nowrap; }
  .contact svg { width: 16px; height: 16px; }
  .contact-web { left: 36px; top: 732px; }
  .contact-mail { right: 34px; top: 718px; }
  .contact-phone { right: 110px; top: 740px; }
</style>
</head>
<body>
  <main class="flyer">
    <svg class="flyer-shapes" viewBox="0 0 540 764" aria-hidden="true">
      <path d="M0 330 C140 300 360 340 540 250 L540 680 C380 716 170 716 0 688 Z" fill="var(--teal)"/>
      <path d="M0 330 C140 300 360 340 540 250" fill="none" stroke="var(--navy)" stroke-width="6"/>
      <path d="M0 688 C170 716 380 716 540 680 L540 694 C380 732 170 732 0 702 Z" fill="var(--navy)"/>
    </svg>

    <div class="hero-photo" role="img" aria-label="Photo of a smiling woman seated in a dental chair"></div>
    <div class="headrest" role="img" aria-label="Blue dental chair headrest"></div>

    <div class="brand"><span class="brand-dot"></span><span class="brand-name">Brightpath Dentistry</span></div>

    <div class="call-pill">
      <div class="call-label">Call or Text Us Now:</div>
      <div class="call-number">555.204.7318</div>
    </div>

    <div class="circle photo-family" role="img" aria-label="Photo of a happy family of four"></div>
    <div class="circle photo-kids" role="img" aria-label="Photo of two smiling children"></div>
    <div class="circle offer offer-treatment">15% off on<br>Treatment<br>Plan</div>
    <div class="circle offer offer-kids">Free Kids<br>Dental<br>Screening</div>
    <div class="circle offer offer-adults">$25 Adults<br>Dental<br>Screening</div>

    <div class="tooth-art" role="img" aria-label="Illustration of a white tooth wearing a gold crown"></div>

    <h1 class="headline">Grand Opening</h1>
    <div class="hours-pill">CONVENIENT <strong>EVENING &amp; SATURDAY</strong> HOURS</div>
    <p class="fine-print">Opening special offers valid until June 15, 2017 by Appointment only</p>
    <p class="welcome">NEW PATIENTS ARE WELCOME!</p>

    <div class="contact contact-web">
      <svg viewBox="0 0 16 16"><circle cx="8" cy="8" r="7" fill="var(--teal)"/><path d="M5 8h6M8 5l3 3-3 3" stroke="#fff" stroke-width="1.6" fill="none"/></svg>
      www.BrightpathDental.com
    </div>
    <div class="contact contact-mail">
      <svg viewBox="0 0 16 16"><circle cx="8" cy="8" r="7" fill="var(--teal)"/><rect x="4" y="5.5" width="8" height="5.5" fill="none" stroke="#fff" stroke-width="1.2"/><path d="M4 5.5l4 3 4-3" stroke="#fff" stroke-width="1.2" fill="none"/></svg>
      info@BrightpathDental.com
    </div>
    <div class="contact contact-phone">
      <svg viewBox="0 0 16 16"><circle cx="8" cy="8" r="7" fill="var(--teal)"/><path d="M5.5 4.5l1.5 0 .8 2-1 .8a5 5 0 0 0 2 2l.8-1 2 .8v1.5c-3.5.4-6.5-2.6-6.1-6.1z" fill="#fff"/></svg>
      555-204-7318
    </div>
  </main>
</body>
</html>
```